Brinetide Yacht Management Full Page Ad Flyer

Yacht Management Package also includes the following periodic Monthly services:

Monthly full vessel systems checklist inspections
Diver For Hull Cleaning And Inspection Of Props, Shafts, and Zincs
Interior/Exterior Detailing and scheduled washdowns
Manage Haulout
Pump-out Services
On-call Captain and Crew Services
Updates

Need more time to provide more content to designers and the printing press template file.

Target Market(s)

Vessel owners, motor yachts, sailboats from 25 feet in length up to 125 feet in length. We do not do cruise ships or yachts larger than 125 feet. Someone who has their boat docked at their house or a local marina. We also offer mobile on-site services.

```html
<!DOCTYPE html>
<html lang="en">
<head>
<meta charset="utf-8">
<title>Brinetide Yacht Management – Package Flyer</title>
<link rel="stylesheet" href="https://fonts.googleapis.com/css2?family=Bebas+Neue&family=Oswald:wght@300&family=Montserrat:wght@500;600;700&display=swap">
<style>
  :root {
    --page: #e6e7e9;
    --card: #0a0a0a;
    --gold: #e3b823;
    --white: #ffffff;
    --num-blue: #2a5aa8;
    --ink: #0b0b0b;
  }
  * { margin: 0; padding: 0; box-sizing: border-box; }
  html, body { width: 1200px; height: 852px; overflow: hidden; background: var(--page); }
  .canvas { position: relative; width: 1200px; height: 852px; }
  .flyer {
    position: absolute; left: 108px; top: 77px; width: 983px; height: 697px;
    background: var(--card); overflow: hidden;
  }
  .abs { position: absolute; }
  .brand { left: 63px; top: 80px; width: 234px; text-align: center; color: var(--white); }
  .brand-name { font: 600 33px/1 "Montserrat", sans-serif; letter-spacing: 3px; }
  .brand-sub { font: 500 8px/1 "Montserrat", sans-serif; letter-spacing: 4px; margin-top: 6px; }
  .headline { left: 63px; top: 140px; font-family: "Bebas Neue", sans-serif; font-weight: 400; line-height: .8; }
  .headline .line-gold { color: var(--gold); font-size: 88px; display: block; }
  .headline .line-white { color: var(--white); font-size: 88px; display: block; margin-top: 6px; letter-spacing: -.5px; }
  .package-tag {
    left: 66px; top: 287px; width: 261px; height: 48px; background: var(--gold);
    display: flex; justify-content: space-between; align-items: center;
    padding: 0 30px 0 31px;
    font: 300 31px/1 "Oswald", sans-serif; color: var(--ink);
  }
  .service { color: var(--white); font: 600 15px/19px "Montserrat", sans-serif; }
  .service-num {
    position: absolute; width: 40px; height: 40px; border-radius: 50%;
    background: var(--white); color: var(--num-blue);
    font: 700 16px/40px "Montserrat", sans-serif; text-align: center;
  }
  .service-text { position: absolute; white-space: nowrap; }
  .range { left: 62px; top: 519px; color: var(--white); }
  .range-line { font: 400 24px/21px "Bebas Neue", sans-serif; }
  .range-line.gold { color: var(--gold); }
  .range-note { font: 500 12.6px/16px "Montserrat", sans-serif; margin-top: 2px; }
  .divider { left: 365px; top: 520px; width: 2px; height: 53px; background: var(--white); }
  .badge { left: 408px; top: 461px; width: 160px; height: 160px; }
  .badge-text {
    left: 408px; top: 499px; width: 160px; text-align: center; color: var(--ink);
  }
  .badge-text .strong { font: 400 31px/27px "Bebas Neue", sans-serif; display: block; }
  .badge-text .light { font: 300 26px/27px "Oswald", sans-serif; display: block; letter-spacing: -1px; }
  .contact-call { left: 62px; top: 607px; color: var(--white); font-family: "Bebas Neue", sans-serif; }
  .contact-call .label { font-size: 29px; line-height: 1; display: block; }
  .contact-call .phone { font-size: 47px; line-height: .9; display: block; }
  .address {
    right: 56px; top: 610px; text-align: right; color: var(--white); font-style: normal;
    font: 500 16.5px/19px "Montserrat", sans-serif;
  }
  .address .web { font-weight: 600; }
  .photo {
    position: absolute; width: 236px; height: 236px; border: 3px solid var(--white);
    box-shadow: 0 4px 12px rgba(0,0,0,.6);
  }
  .photo-yacht { left: 638px; top: 39px; background: linear-gradient(180deg, #1f3a34 0%, #2d5a57 55%, #cfd8da 62%, #1d4f55 70%, #133a3e 100%); }
  .photo-polish { left: 638px; top: 339px; background: linear-gradient(135deg, #d9dde2 0%, #eef1f4 40%, #3c4b6b 62%, #f1f2f2 100%); }
  .photo-engine { left: 725px; top: 186px; background: linear-gradient(160deg, #c9ced3 0%, #e3e6e8 35%, #2a2c30 55%, #bfc3c6 100%); }
</style>
</head>
<body>
<div class="canvas">
  <section class="flyer">
    <div class="abs brand">
      <div class="brand-name">BRINETIDE</div>
      <div class="brand-sub">YACHT MANAGEMENT</div>
    </div>

    <h1 class="abs headline">
      <span class="line-gold">YACHT</span>
      <span class="line-white">MANAGEMENT</span>
    </h1>
    <div class="abs package-tag" aria-label="Package">
      <span>P</span><span>A</span><span>C</span><span>K</span><span>A</span><span>G</span><span>E</span>
    </div>

    <div class="abs service" style="left:63px;top:356px">
      <span class="service-num" style="left:0;top:0">01</span>
      <span class="service-text" style="left:56px;top:-14px">Diver For Hull Cleaning<br>&amp; Inspection Of Props,<br>Shafts And Zincs</span>
    </div>
    <div class="abs service" style="left:63px;top:410px">
      <span class="service-num" style="left:0;top:0">02</span>
      <span class="service-text" style="left:56px;top:10px">Manage Haulout</span>
    </div>
    <div class="abs service" style="left:63px;top:458px">
      <span class="service-num" style="left:0;top:0">03</span>
      <span class="service-text" style="left:56px;top:0">Interior/exterior Detailing &amp;<br>Scheduled Washdowns</span>
    </div>
    <div class="abs service" style="left:344px;top:354px">
      <span class="service-num" style="left:0;top:0">04</span>
      <span class="service-text" style="left:56px;top:10px">Pump-out Services</span>
    </div>
    <div class="abs service" style="left:344px;top:400px">
      <span class="service-num" style="left:0;top:0">05</span>
      <span class="service-text" style="left:56px;top:2px;line-height:17px">On-call Captain &amp;<br>Crew Services</span>
    </div>

    <div class="abs range">
      <div class="range-line">SAILBOATS FROM 25 FEET IN</div>
      <div class="range-line gold">LENGTH UP TO 125 FEET IN LENGTH.</div>
      <div class="range-note">Services offered at house or a local marina.</div>
    </div>
    <div class="abs divider"></div>

    <svg class="abs badge" viewBox="0 0 160 160" aria-hidden="true">
      <polygon fill="#e3b823" stroke="#e3b823" stroke-width="10" stroke-linejoin="round"
        points="154,80 140.9,99.8 139.9,123.5 117.6,131.8 102.9,150.4 80,144 57.1,150.4 42.4,131.8 20.1,123.5 19.1,99.8 6,80 19.1,60.2 20.1,36.5 42.4,28.2 57.1,9.6 80,16 102.9,9.6 117.6,28.2 139.9,36.5 140.9,60.2"/>
    </svg>
    <div class="abs badge-text">
      <span class="strong">MOBILE</span>
      <span class="light">ON-SITE</span>
      <span class="strong">SERVICE</span>
    </div>

    <div class="abs contact-call">
      <span class="label">CALL US TODAY</span>
      <span class="phone">014-726-395</span>
    </div>

    <address class="abs address">
      48 Harbor Lane<br>
      Millbrook, PA 19870<br>
      <span class="web">www.brinetideyachts.com</span>
    </address>

    <div class="photo photo-yacht" role="img" aria-label="Photo of a white luxury motor yacht cruising on dark green water"></div>
    <div class="photo photo-polish" role="img" aria-label="Photo of a technician in gloves machine-polishing a white boat hull"></div>
    <div class="photo photo-engine" role="img" aria-label="Photo of a mechanic servicing an open outboard engine on a boat stern"></div>
  </section>
</div>
</body>
</html>
```